Logo and packaging for Electronic Disposable Shisha
We are a new company launching a Disposable Electronic Shisha that last up to 600 puff that comes in different colours and flavour as: blueberry, strawberry,apple, chocolate, and fruit mix . The logo should communicate elegance, style life and gold as the one color only . The name is ZYVO (e-shisha) , The idea is having the logo on capital letter and e-shiha at the footer of the logo,Could be just letters or letters and logo You guys are the experts so please show me your creativity! The product will come in 2 presentation,on individual tube as in the image and "cigarette box style with 5 eshishas" We need the design of the logo and packaging of the cigarette package,on the package the logo and edges will be on gold stamping and should contain all the flavours (blueberry,strawberry,apple,chocolate and mint) You can play with the color of the background and images. Thank You!
+18
Cigarette
ZYVO (e-shisha)

```html
<!DOCTYPE html>
<html lang="en">
<head>
<meta charset="UTF-8">
<title>ZYVO e-shisha pack</title>
<link rel="stylesheet" href="https://fonts.googleapis.com/css2?family=Tinos:wght@400;700&display=swap">
<style>
  :root {
    --page: #ffffff;
    --pack: #000000;
    --gold-light: #f1dca0;
    --gold: #d9b86a;
    --gold-deep: #a8843a;
    --gold-text: #c9a555;
  }
  html, body {
    margin: 0;
    padding: 0;
    width: 1200px;
    height: 1000px;
    overflow: hidden;
    background: var(--page);
  }
  .canvas {
    position: relative;
    width: 1200px;
    height: 1000px;
  }
  .pack {
    position: absolute;
    left: 380px;
    top: 112px;
    width: 440px;
    height: 776px;
    box-sizing: border-box;
    background: var(--pack);
    border: 3px solid var(--gold-light);
    box-shadow: inset 0 0 0 2px var(--gold);
  }
  .pack__lid-line {
    position: absolute;
    left: 0;
    right: 0;
    top: 176px;
    height: 4px;
    background: var(--gold-light);
    border-top: 1px solid var(--gold);
    border-bottom: 1px solid var(--gold);
  }
  .pack__ornament {
    position: absolute;
    left: 112px;
    top: 232px;
    width: 210px;
    height: 42px;
    background: radial-gradient(ellipse at center, rgba(217,184,106,0.4), rgba(217,184,106,0) 70%);
  }
  .pack__brand {
    position: absolute;
    left: 0;
    right: 0;
    top: 299px;
    margin: 0;
    text-align: center;
    font-family: "Tinos", "Times New Roman", serif;
    font-weight: 700;
    font-size: 96px;
    line-height: 1;
    letter-spacing: 8px;
    padding-left: 8px;
    background: linear-gradient(180deg, var(--gold-deep) 0%, var(--gold-light) 45%, var(--gold) 60%, var(--gold-deep) 100%);
    -webkit-background-clip: text;
    background-clip: text;
    color: transparent;
  }
  .pack__flavours {
    position: absolute;
    left: 150px;
    top: 425px;
    width: 136px;
    height: 170px;
    border-radius: 50%;
    background: radial-gradient(ellipse at 50% 40%, #b0302a 0%, #6b3a28 35%, #3a4f8a 55%, rgba(0,0,0,0) 72%);
  }
  .pack__tagline {
    position: absolute;
    left: 0;
    right: 0;
    top: 675px;
    margin: 0;
    text-align: center;
    font-family: "Tinos", "Times New Roman", serif;
    font-weight: 400;
    font-size: 38px;
    line-height: 1;
    letter-spacing: 10px;
    padding-left: 10px;
    color: var(--gold-text);
  }
</style>
</head>
<body>
<div class="canvas">
  <div class="pack">
    <div class="pack__lid-line"></div>
    <div class="pack__ornament" role="img" aria-label="Gold swirl flourish ornament above the brand name"></div>
    <h1 class="pack__brand">ZYVO</h1>
    <div class="pack__flavours" role="img" aria-label="Illustration of flavours: apple, chocolate bar, blueberries, mint leaf and strawberry with reflection"></div>
    <p class="pack__tagline">e-shisha</p>
  </div>
</div>
</body>
</html>
```